Ledge Crafts one page flyer

We need a standard A4 size flyer for a new company called Ledge Crafts. We are a construction material company and sell trims, crown mouldings, baseboards and panelings.
We would like to see the design with the following information:
1. Size: A4
2. Only one front page, no design need to display on back
3. Logo (Ledge Crafts, see the attached EPS file)
4. Slogan: We offer high quality products for competitive prices.
5. Content please see the PDF file
6. The production has 2 category, one called "Crown Moulding", the other is "Wainscoting", Crown Moulding has 5 productions, wainscoting has 2 production(Details see PDF file)
6. We temporary only can provide low resolution images for 7 productions, only the winner will be provided with High Resolution images.
Look and feel
Each slider illustrates characteristics of the customer's brand and the style your logo design should communicate.

```html
<!DOCTYPE html>
<html lang="en">
<head>
<meta charset="utf-8">
<title>Ledge Crafts – Flyer</title>
<link href="https://fonts.googleapis.com/css2?family=Montserrat:wght@400;500;600;700&display=swap" rel="stylesheet">
<style>
  :root {
    --brand-blue: #1f4fa3;
    --brand-blue-light: #2f66bd;
    --slate: #4d5a66;
    --ink: #2a2a2a;
    --rule: #5b6570;
    --frame: #3a3a3a;
    --bracket: #b9babd;
    --paper: #ffffff;
    --tile-tone-a: #e4e6ea;
    --tile-tone-b: #f7f8fa;
  }
  * { box-sizing: border-box; margin: 0; padding: 0; }
  html, body {
    width: 1109px; height: 1200px; overflow: hidden;
    background: var(--paper);
    font-family: "Montserrat", sans-serif;
  }
  .flyer {
    position: relative; width: 1109px; height: 1200px;
    background: linear-gradient(135deg, #ffffff 0%, #f6f7f8 45%, #ffffff 100%);
  }
  .frame {
    position: absolute; left: 58px; top: 46px; width: 994px; height: 1107px;
    border: 1px solid var(--frame);
  }
  .bracket { position: absolute; width: 0; height: 0; }
  .bracket--top-left::before, .bracket--top-left::after,
  .bracket--bottom-right::before, .bracket--bottom-right::after {
    content: ""; position: absolute; background: var(--bracket);
  }
  .bracket--top-left { left: 47px; top: 39px; }
  .bracket--top-left::before { left: 0; top: 0; width: 103px; height: 14px; }
  .bracket--top-left::after { left: 0; top: 0; width: 18px; height: 152px; }
  .bracket--bottom-right { left: 1061px; top: 1160px; }
  .bracket--bottom-right::before { right: 0; bottom: 0; width: 132px; height: 14px; }
  .bracket--bottom-right::after { right: 0; bottom: 0; width: 18px; height: 152px; }

  .brand {
    position: absolute; left: 0; right: 0; top: 98px;
    display: flex; justify-content: center; align-items: center; gap: 24px;
  }
  .brand__mark {
    width: 86px; height: 86px; border: 12px solid var(--bracket);
  }
  .brand__name {
    font-weight: 500; font-size: 60px; letter-spacing: 4px;
    color: var(--slate); line-height: 1;
  }
  .brand__tagline {
    font-weight: 400; font-size: 19px; letter-spacing: 6.5px;
    color: var(--slate); margin-top: 14px; text-align: right;
  }
  .rule { position: absolute; height: 3px; background: var(--rule); }
  .rule--top { left: 146px; width: 817px; top: 216px; }
  .rule--bottom { left: 116px; width: 877px; top: 948px; }

  .headline {
    position: absolute; left: 0; right: 0; top: 240px; text-align: center;
    font-size: 37px; line-height: 40px; text-transform: uppercase;
  }
  .headline__strong { font-weight: 700; color: var(--slate); display: block; }
  .headline__soft { font-weight: 400; color: var(--ink); display: block; }

  .category {
    position: absolute; left: 365px; width: 374px; height: 60px;
    border-radius: 30px;
    background: linear-gradient(90deg, var(--brand-blue), var(--brand-blue-light));
    color: #fff; font-weight: 700; font-size: 24px;
    display: flex; align-items: center; justify-content: center;
    box-shadow: 0 10px 8px -8px rgba(0,0,0,0.45);
  }
  .category--crown { top: 361px; }
  .category--wainscot { top: 707px; }

  .product {
    position: absolute; width: 165px; height: 93px;
    border: 1.5px solid var(--brand-blue); border-radius: 28px;
    background: var(--paper);
  }
  .product__image {
    position: absolute; inset: 12px 22px; border-radius: 12px;
    background: linear-gradient(135deg, var(--tile-tone-a), var(--tile-tone-b));
  }

  .info {
    position: absolute; top: 986px; font-weight: 600; font-size: 15px;
    line-height: 17px; color: var(--ink);
  }
  .info__title {
    font-weight: 700; font-size: 24px; line-height: 28px;
    color: var(--brand-blue); margin-bottom: 18px;
  }
  .info--hours { left: 116px; text-align: left; }
  .info--contact { left: 405px; width: 300px; text-align: center; }
  .info--warehouse { right: 150px; text-align: right; }
</style>
</head>
<body>
<main class="flyer">
  <div class="frame"></div>
  <div class="bracket bracket--top-left"></div>
  <div class="bracket bracket--bottom-right"></div>

  <header class="brand">
    <div class="brand__mark"></div>
    <div>
      <div class="brand__name">LEDGE CRAFTS</div>
      <div class="brand__tagline">FOR ALL TYPES OF PROJECTS</div>
    </div>
  </header>
  <div class="rule rule--top"></div>

  <h1 class="headline">
    <span class="headline__strong">We offer high quality</span>
    <span class="headline__soft">Products for competitive prices</span>
  </h1>

  <div class="category category--crown">Crown Moulding</div>
  <div class="product" style="left:284px;top:457px"><div class="product__image" role="img" aria-label="Crown moulding profile"></div></div>
  <div class="product" style="left:473px;top:457px"><div class="product__image" role="img" aria-label="Crown moulding profile"></div></div>
  <div class="product" style="left:662px;top:457px"><div class="product__image" role="img" aria-label="Crown moulding profile"></div></div>
  <div class="product" style="left:188px;top:571px"><div class="product__image" role="img" aria-label="Crown moulding profile"></div></div>
  <div class="product" style="left:377px;top:571px"><div class="product__image" role="img" aria-label="Crown moulding profile"></div></div>
  <div class="product" style="left:567px;top:571px"><div class="product__image" role="img" aria-label="Crown moulding profile"></div></div>
  <div class="product" style="left:755px;top:571px"><div class="product__image" role="img" aria-label="Crown moulding profile"></div></div>

  <div class="category category--wainscot">Wainscoting</div>
  <div class="product" style="left:377px;top:799px"><div class="product__image" role="img" aria-label="Wainscoting profile"></div></div>
  <div class="product" style="left:567px;top:799px"><div class="product__image" role="img" aria-label="Wainscoting profile"></div></div>

  <div class="rule rule--bottom"></div>

  <section class="info info--hours">
    <h2 class="info__title">Office Hours:</h2>
    <p>Mon – Fri: 7:00am – 6.00pm</p>
    <p>Saturdays: 8:00am – 4.00pm</p>
    <p>Sundays: Closed</p>
  </section>
  <section class="info info--contact">
    <h2 class="info__title">Contact Information</h2>
    <p>Ledge Crafts</p>
    <p>Office:</p>
    <p>412 Maple Grove Rd, unit 4</p>
    <p>Aurora, Ontario L7G 2K1</p>
    <p>Phone: 905-555-0142</p>
    <p>info@ledgecrafts.ca</p>
  </section>
  <section class="info info--warehouse">
    <h2 class="info__title">Warehouse:</h2>
    <p>88 Birchfield Ave</p>
    <p>Markham, ON L3R 4T6</p>
    <p>By Appointment Only</p>
  </section>
</main>
</body>
</html>
```